Trifold Brochure needed for Hearthline Counseling

Hi! We need to have a trifold brochure made.

We would like to see brochure designs that use our logo colors, which are khaki, chocolate brown, and gray.

The brochure should be a modern design and please use your creativity.

Brochure is a trifold brochure, size is 8.5 x 11 and full color.

The following attachment has the content to be used in the trifold brochure, as well as some possible pictures. I have also attached our logo.

We would like to use file #2 for sure (picture number 31759204) and add the quote from her...

"At first, I was reluctant about going to Hearthline. Once I got there, I was glad I went. I learned a lot and was treated like family the whole time." Marlene Oakes

Requirements
Must have
• Our logo
• Information should be listed exactly as the attached document
• You must stick with our logo colors

```html
<!DOCTYPE html>
<html lang="en">
<head>
<meta charset="utf-8">
<title>Hearthline Counseling – Trifold Brochure</title>
<link rel="stylesheet" href="https://fonts.googleapis.com/css2?family=Tinos:ital,wght@0,400;0,700;1,400&family=Arimo:ital,wght@0,400;1,400&display=swap">
<style>
  :root {
    --cream: #f1ece0;
    --cream-light: #f7f4ec;
    --khaki: #d6cba8;
    --gray-band: #aca69d;
    --gray-quote: #bbb6ae;
    --brown: #6b4a2e;
    --ink: #1c1a17;
    --logo-gray: #8d8a86;
    --white: #ffffff;
  }
  * { margin: 0; padding: 0; box-sizing: border-box; }
  html, body { width: 1200px; height: 927px; overflow: hidden; }
  body {
    font-family: "Tinos", "Times New Roman", serif;
    color: var(--ink);
    background: var(--cream);
  }
  .brochure {
    position: relative;
    width: 1200px;
    height: 927px;
    background: radial-gradient(ellipse at 55% 45%, var(--cream-light) 0%, var(--cream) 55%, #e6dfcf 100%);
    overflow: hidden;
  }
  .abs { position: absolute; }

  /* Left panel */
  .tagline-block {
    left: 0; top: 0; width: 398px; height: 190px;
    background: var(--khaki);
  }
  .tagline {
    left: 33px; top: 92px;
    font-size: 20px;
    white-space: nowrap;
  }
  .tagline .initial { font-size: 29px; }
  .photo-couple-leaves {
    left: 15px; top: 311px; width: 383px; height: 251px;
    background: linear-gradient(160deg, #eae3d2 0%, #c9a878 45%, #9a6a3c 75%, #7a4f2c 100%);
  }
  .rule-left {
    left: 15px; top: 582px; width: 383px; height: 2px;
    background: var(--white);
  }
  .band-left {
    left: 15px; top: 590px; width: 383px; height: 48px;
    background: var(--gray-band);
  }
  .logo {
    left: 18px; top: 700px; width: 370px;
    display: flex; align-items: center; gap: 16px;
  }
  .logo-dot {
    flex: none;
    width: 50px; height: 50px; border-radius: 50%;
    background: var(--logo-gray);
  }
  .logo-name {
    font-size: 46px;
    line-height: 1.05;
    color: var(--brown);
    font-weight: 400;
  }

  /* Middle panel */
  .intro {
    left: 403px; top: 20px; width: 370px;
    font-size: 14.5px; line-height: 1.25;
    white-space: nowrap;
  }
  .photo-woman-lake {
    left: 403px; top: 134px; width: 357px; height: 250px;
    background: linear-gradient(180deg, #9fb8bd 0%, #c3cfc9 40%, #7e8f7a 70%, #4f5a44 100%);
  }
  .quote-box {
    left: 403px; top: 392px; width: 357px; height: 76px;
    background: var(--gray-quote);
    padding: 12px 8px 0 8px;
    font-family: "Arimo", Arial, sans-serif;
    font-style: italic;
    font-size: 9.6px; line-height: 1.4;
    white-space: nowrap;
  }
  .reasons-title {
    left: 403px; top: 545px; width: 380px;
    text-align: center;
    font-weight: 700; font-size: 17.5px;
  }
  .reasons {
    left: 410px; top: 597px; width: 385px;
    list-style: none;
    font-size: 16px; line-height: 1.3;
    white-space: nowrap;
  }
  .reasons li { margin-bottom: 18px; }
  .reasons .indent { padding-left: 14px; display: block; }

  /* Right panel */
  .strip-right {
    left: 802px; top: 70px; width: 398px; height: 9px;
    background: var(--white);
  }
  .panel-right {
    left: 802px; top: 79px; width: 398px; height: 540px;
    background: linear-gradient(180deg, var(--cream-light) 0%, var(--cream) 100%);
  }
  .benefits {
    left: 815px; top: 104px; width: 375px;
    list-style: none;
    font-size: 14px; line-height: 1.3;
    white-space: nowrap;
  }
  .benefits li { margin-bottom: 27px; }
  .ripple {
    left: 815px; top: 508px; width: 380px;
    font-weight: 700; font-size: 15.5px; line-height: 1.3;
    white-space: nowrap;
  }
  .photo-couple-piggyback {
    left: 889px; top: 653px; width: 194px; height: 240px;
    background: radial-gradient(ellipse at 50% 45%, #d9b89a 0%, #e9dccb 55%, #f6f3ee 100%);
  }
</style>
</head>
<body>
<main class="brochure">

  <!-- Left panel -->
  <div class="abs tagline-block"></div>
  <p class="abs tagline"><span class="initial">M</span>aking Solutions "1" Patient at a Time</p>
  <div class="abs photo-couple-leaves" role="img" aria-label="Photo of a smiling older couple lying in autumn leaves"></div>
  <div class="abs rule-left"></div>
  <div class="abs band-left"></div>
  <div class="abs logo">
    <span class="logo-dot"></span>
    <span class="logo-name">Hearthline<br>Counseling</span>
  </div>

  <!-- Middle panel -->
  <p class="abs intro"><b>Hearthline</b> is Pro-active Opioid Education / not for addicts<br>or problem patients. <b>Hearthline</b> only sees <b>Good Patients</b>,<br>because problem patients and addicts <b>do not</b> want<br>education they only<br>want pills.</p>
  <div class="abs photo-woman-lake" role="img" aria-label="Photo of a smiling older woman beside a lake"></div>
  <blockquote class="abs quote-box">"At first, I was reluctant about going to Hearthline. Once I got there, I was glad<br>I went. I learned a lot and was treated like family the whole time."<br>" Marlene Oakes</blockquote>

  <h2 class="abs reasons-title">We Educate Good Patients Because:</h2>
  <ol class="abs reasons">
    <li>1. <b>Good Patients</b> are Receptive to new information</li>
    <li>2. <b>Education" Good Patients</b> need it the least!<span class="indent">Therefore their minds are open and will</span><span class="indent">soak it up the Most.</span></li>
    <li>3. Hearthline will <b>Teach You</b> and Hopefully <b>You</b> will<span class="indent"><b>Teach someone else</b>, Better than that,</span><span class="indent">maybe <b>Your</b> Education will <b>Save someone else.</b></span></li>
  </ol>

  <!-- Right panel -->
  <div class="abs strip-right"></div>
  <div class="abs panel-right"></div>
  <ul class="abs benefits">
    <li><b>Education</b> helps patients understand, predict and<br>manage their pain cycles.</li>
    <li><b>Education</b> lessens negative thinking and emotional stress</li>
    <li><b>Education</b> teaches coping skills to minimize pain and to<br>maximize active involvement<br>in positive like experiences.</li>
    <li><b>Educating</b> Your Patients will mean more effective use of<br>your medical services, meaning fewer unnecessary<br>phone calls to your staff.</li>
    <li><b>Education</b> Equals improved Compliance, which means<br>more Compliant urine drug<br>screens.</li>
  </ul>
  <p class="abs ripple">One Patient's Education can Positively affect a<br>Family; that One Family can Positively affect One<br>Neighborhood: One Neighborhood can Positively<br>affect One Community; One Community at a time,<br>can Change Society.</p>
  <div class="abs photo-couple-piggyback" role="img" aria-label="Photo of an older man giving a smiling woman a piggyback ride"></div>

</main>
</body>
</html>
```